Letterhead design for BRENLOW company

I need an A4 letterhead design for my company "Brenlow Electrical Products". I need the letterhead to match my current logo and business card designs. I would like it to be colourful and match the design of the business card in terms of the flowing line of colour where the information is.  

Target Market(s)

Adults aged 20 - 50 Upper middle class.

Industry/Entity Type

It Company

Requirements
Must have
• Must be A4 size and match my current logo and business card designs. Must be clean simple and eye catching.

• Must have the following information

• Brenlow Electrical Products LTD
• 7 Dunmere Lane
• Chiswick
• London
• England
• N9 3KD
• Company No. 05413926
• VAT No. GB 731552804

• Telephone: 02036159402
• Mobile: 07815263470
• Email: info@brenlow-products.co.uk
Nice to have
• nice to have a wave of colour like the business card.
Should not have
• Should not be a different colour scheme to the business card and logo design.

```html
<!DOCTYPE html>
<html lang="en">
<head>
<meta charset="utf-8">
<title>Brenlow Electrical Products – Letterhead</title>
<link rel="stylesheet" href="https://fonts.googleapis.com/css2?family=Didact+Gothic&family=Source+Sans+3:wght@400&display=swap">
<style>
  :root {
    --teal-deep: #1a9aa6;
    --teal-soft: #bfeff0;
    --brand-blue: #2a88b8;
    --link-blue: #1a8ae6;
    --ink: #1a1a1a;
    --paper: #ffffff;
    --paper-shade: #e9e9e9;
    --backdrop: #d9d9d9;
  }
  html, body {
    margin: 0;
    padding: 0;
    width: 927px;
    height: 1200px;
    overflow: hidden;
    background: var(--backdrop);
  }
  .letterhead {
    position: absolute;
    left: 39px;
    top: 0;
    width: 849px;
    height: 1200px;
    overflow: hidden;
    background:
      radial-gradient(ellipse 520px 640px at 430px 440px, var(--paper) 55%, rgba(255,255,255,0) 100%),
      linear-gradient(180deg, #f9f9f9 0%, #f7f7f7 60%, var(--paper-shade) 100%);
  }
  .wave {
    position: absolute;
    display: block;
  }
  .wave-top { right: 0; top: 0; }
  .wave-bottom { left: 0; bottom: 0; }
  .brand {
    position: absolute;
    left: 48px;
    top: 44px;
    color: var(--brand-blue);
    font-family: "Didact Gothic", sans-serif;
    font-weight: 400;
  }
  .brand-name {
    display: block;
    font-size: 60px;
    line-height: 64px;
    letter-spacing: 1px;
  }
  .brand-sub {
    display: block;
    margin-top: 2px;
    font-size: 20px;
    letter-spacing: 1.2px;
  }
  .contact {
    position: absolute;
    top: 1086px;
    font-family: "Source Sans 3", sans-serif;
    font-size: 12px;
    line-height: 15.2px;
    color: var(--ink);
  }
  .contact p { margin: 0; white-space: nowrap; }
  .contact-company { left: 484px; }
  .contact-lines { left: 659px; top: 1101.2px; }
  .company-name { color: var(--link-blue); }
  .contact-lines .label {
    display: inline-block;
    width: 15px;
    color: var(--link-blue);
  }
</style>
</head>
<body>
<main class="letterhead">
  <svg class="wave wave-top" width="360" height="140" viewBox="0 0 360 140" role="img" aria-label="Teal wave of colour across the top corner">
    <defs>
      <linearGradient id="waveTopFill" x1="0" y1="0" x2="1" y2="0">
        <stop offset="0" stop-color="var(--teal-deep)"/>
        <stop offset="1" stop-color="var(--teal-soft)"/>
      </linearGradient>
    </defs>
    <path d="M0 0 Q150 150 360 118 L360 0 Z" fill="url(#waveTopFill)"/>
  </svg>

  <svg class="wave wave-bottom" width="390" height="140" viewBox="0 0 390 140" role="img" aria-label="Teal wave of colour across the bottom corner">
    <defs>
      <linearGradient id="waveBottomFill" x1="1" y1="0" x2="0" y2="0">
        <stop offset="0" stop-color="var(--teal-deep)"/>
        <stop offset="1" stop-color="var(--teal-soft)"/>
      </linearGradient>
    </defs>
    <path d="M0 22 Q230 -14 388 140 L0 140 Z" fill="url(#waveBottomFill)"/>
  </svg>

  <header class="brand">
    <span class="brand-name">BRENLOW</span>
    <span class="brand-sub">Electrical Products</span>
  </header>

  <footer>
    <div class="contact contact-company">
      <p class="company-name">Brenlow Electrical Products LTD</p>
      <p>7 Dunmere Lane, Chiswick,</p>
      <p>London, England, N9 3KD</p>
      <p>Company No. 05413926</p>
      <p>VAT No. GB 731552804</p>
    </div>
    <div class="contact contact-lines">
      <p><span class="label">P.</span>02036159402</p>
      <p><span class="label">M.</span>07815263470</p>
      <p><span class="label">E.</span>info@brenlow-products.co.uk</p>
      <p><span class="label">W.</span>www.brenlow-products.co.uk</p>
    </div>
  </footer>
</main>
</body>
</html>
```